Ayurvedic Beauty Company in Need of Business Cards

My company is a high-end ayurvedic beauty brand. I need a business card that represents that. The designer should utilize logo and color palette. I want these cards to be printed with the foil accents so keep that in mind.

I have attached the ai of my logo and business card info. As well as, some of the product we are launching soon, they do not have to be on the card.

Be creative and have fun.

Thanks in advance,

Marla

```html
<!DOCTYPE html>
<html lang="en">
<head>
<meta charset="utf-8">
<title>Aurum Veda Business Card</title>
<link rel="stylesheet" href="https://fonts.googleapis.com/css2?family=Oswald:wght@600&family=Open+Sans:wght@400;600&display=swap">
<style>
  :root {
    --backdrop: #2a2a2a;
    --card: #1b1b1b;
    --ink-white: #f4f4f4;
    --foil-gold: #e9a73b;
    --foil-silver: #b9b9b9;
    --rule-grey: #6a6a6a;
  }
  * { box-sizing: border-box; margin: 0; padding: 0; }
  html, body {
    width: 1200px; height: 1200px; overflow: hidden;
    background: var(--backdrop);
    font-family: "Open Sans", sans-serif;
  }
  .stage {
    width: 1200px; height: 1200px;
    display: flex; flex-direction: column; align-items: center; justify-content: center;
    gap: 44px;
  }
  .card {
    position: relative;
    width: 900px; height: 514px;
    background: var(--card);
    box-shadow: 0 10px 30px rgba(0,0,0,.45);
  }
  .card-front { display: flex; align-items: center; justify-content: center; }
  .brand-name {
    font-family: "Open Sans", sans-serif;
    font-weight: 600;
    font-size: 40px;
    letter-spacing: 6px;
    text-transform: uppercase;
    color: var(--foil-silver);
  }
  .identity {
    position: absolute; right: 470px; top: 170px;
    text-align: right;
  }
  .person-name {
    font-family: "Oswald", sans-serif;
    font-weight: 600;
    font-size: 56px;
    line-height: 1;
    color: var(--ink-white);
    text-transform: uppercase;
    letter-spacing: 1px;
  }
  .person-title {
    margin-top: 14px;
    font-size: 30px;
    letter-spacing: 2px;
    color: var(--foil-gold);
  }
  .divider {
    position: absolute; left: 455px; top: 176px;
    width: 3px; height: 140px;
    background: var(--rule-grey);
  }
  .contact-list {
    position: absolute; left: 482px; top: 188px;
    list-style: none;
  }
  .contact-item {
    display: flex; align-items: center;
    height: 31px;
    font-size: 23px;
    color: var(--ink-white);
  }
  .contact-item svg { width: 20px; height: 20px; margin-right: 30px; fill: var(--foil-gold); flex: none; }
  .address {
    position: absolute; left: 220px; top: 412px;
    display: flex; align-items: center;
    font-size: 26px; letter-spacing: 1.5px;
    color: var(--ink-white);
  }
  .address svg { width: 22px; height: 28px; margin-right: 22px; fill: var(--foil-gold); }
</style>
</head>
<body>
<main class="stage">
  <section class="card card-front">
    <span class="brand-name">Aurum Veda</span>
  </section>

  <section class="card card-back">
    <div class="identity">
      <h1 class="person-name">Marla Devane</h1>
      <p class="person-title">CEO</p>
    </div>
    <div class="divider"></div>
    <ul class="contact-list">
      <li class="contact-item">
        <svg viewBox="0 0 24 24"><path d="M6.6 10.8a15 15 0 0 0 6.6 6.6l2.2-2.2c.3-.3.7-.4 1-.2 1.1.4 2.3.6 3.6.6.6 0 1 .4 1 1V20c0 .6-.4 1-1 1A17 17 0 0 1 3 4c0-.6.4-1 1-1h3.5c.6 0 1 .4 1 1 0 1.3.2 2.5.6 3.6.1.3 0 .7-.2 1z"/></svg>
        1(555) 240-7138
      </li>
      <li class="contact-item">
        <svg viewBox="0 0 24 24"><path d="M12 5C7 5 2.5 6.5 1 9v3h5V9.5c1.8-.6 10.2-.6 12 0V12h5V9c-1.5-2.5-6-4-11-4zM7 13l-3 6h16l-3-6H7zm5 1.5a2 2 0 1 1 0 4 2 2 0 0 1 0-4z"/></svg>
        1(555) 610-3384
      </li>
      <li class="contact-item">
        <svg viewBox="0 0 24 24"><path d="M2 5h20v14H2zm2 2v.4l8 5.3 8-5.3V7zm0 2.8V17h16V9.8l-8 5.3z"/></svg>
        marla@aurumveda.com
      </li>
      <li class="contact-item">
        <svg viewBox="0 0 24 24"><path d="M12 2a10 10 0 1 0 0 20 10 10 0 0 0 0-20zm-1 2.1V8H7.6A8 8 0 0 1 11 4.1zm2 0A8 8 0 0 1 16.4 8H13zM6.6 10H11v4H6.6a8 8 0 0 1 0-4zm6.4 0h4.4a8 8 0 0 1 0 4H13zm-5.4 6H11v3.9A8 8 0 0 1 7.6 16zm5.4 0h3.4a8 8 0 0 1-3.4 3.9z"/></svg>
        www.aurumveda.com
      </li>
    </ul>
    <p class="address">
      <svg viewBox="0 0 22 28"><path d="M11 0A11 11 0 0 0 0 11c0 8 11 17 11 17s11-9 11-17A11 11 0 0 0 11 0zm0 15a4 4 0 1 1 0-8 4 4 0 0 1 0 8z"/></svg>
      Your Street Address, Singapore, 1234
    </p>
  </section>
</main>
</body>
</html>
```